Design a new business card

Time for an update on the business cards!
We want to keep the logo, and keep the colors predominantly Black, red and white.
White logo, black background, red/white highlights and/or accents.
Have attached the logo, but this is not the color we want.
Business card should have room for all usual fields.

```html
<!DOCTYPE html>
<html lang="en">
<head>
<meta charset="utf-8">
<title>Halvor Finance – Business Card</title>
<link href="https://fonts.googleapis.com/css2?family=Lato:wght@400;700;900&display=swap" rel="stylesheet">
<style>
  :root {
    --stage: #2b2d31;
    --card-black: #1c1c1e;
    --accent-red: #ee2f3a;
    --ink-white: #ffffff;
    --ink-soft: #d9d9d9;
    --icon-grey: #bfbfbf;
  }
  * { margin: 0; padding: 0; box-sizing: border-box; }
  html, body {
    width: 1200px; height: 900px; overflow: hidden;
    background: var(--stage);
    font-family: "Lato", sans-serif;
  }
  .stage {
    width: 1200px; height: 900px;
    display: flex; align-items: center; justify-content: center; gap: 90px;
  }
  .card {
    position: relative; width: 360px; height: 620px;
    background: var(--card-black); overflow: hidden;
    box-shadow: 0 18px 40px rgba(0,0,0,.45);
  }
  .card-shapes { position: absolute; inset: 0; }
  .brand {
    position: absolute; left: 0; right: 0;
    display: flex; align-items: center; justify-content: center; gap: 10px;
    color: var(--ink-white); font-weight: 700; font-size: 24px; letter-spacing: 2px;
    text-transform: uppercase;
  }
  .brand-dot { width: 12px; height: 12px; border-radius: 50%; background: var(--ink-white); }
  .card-front .brand { top: 120px; }
  .card-back .brand { top: 110px; }
  .holder { position: absolute; left: 40px; top: 360px; color: var(--ink-white); }
  .holder-name { font-size: 22px; font-weight: 900; letter-spacing: 1px; text-transform: uppercase; }
  .holder-role { margin-top: 10px; font-size: 16px; line-height: 1.35; color: var(--ink-soft); }
  .contact-list { position: absolute; left: 40px; top: 480px; list-style: none; }
  .contact-item {
    display: flex; align-items: center; gap: 14px; height: 36px;
    color: var(--ink-soft); font-size: 13px;
  }
  .contact-icon {
    width: 22px; height: 22px; border-radius: 50%; background: var(--icon-grey);
    display: flex; align-items: center; justify-content: center;
  }
  .web-line {
    position: absolute; right: 70px; bottom: 140px;
    display: flex; align-items: center; gap: 12px;
    color: var(--ink-white); font-size: 13px;
  }
  .web-line .contact-icon { background: transparent; border: 1.5px solid var(--ink-white); }
</style>
</head>
<body>
<main class="stage">

  <article class="card card-front">
    <svg class="card-shapes" viewBox="0 0 360 620" aria-hidden="true">
      <polygon points="0,0 220,0 360,0 360,250 0,290" fill="var(--accent-red)"/>
      <polygon points="230,0 360,0 360,150 300,260" fill="var(--card-black)"/>
      <polygon points="0,250 300,228 0,262" fill="var(--card-black)"/>
      <polygon points="0,272 300,238 360,250 360,262 0,290" fill="var(--card-black)"/>
    </svg>
    <div class="brand"><span class="brand-dot"></span>Halvor Finance</div>
    <div class="holder">
      <h1 class="holder-name">Anika Solberg</h1>
      <p class="holder-role">Accountant and<br>Tax Consultant</p>
    </div>
    <ul class="contact-list">
      <li class="contact-item">
        <span class="contact-icon"><svg width="12" height="10" viewBox="0 0 12 10"><rect x="0.5" y="0.5" width="11" height="9" fill="none" stroke="#1c1c1e"/><polyline points="0.5,0.5 6,5.5 11.5,0.5" fill="none" stroke="#1c1c1e"/></svg></span>
        anika@halvorfin.com
      </li>
      <li class="contact-item">
        <span class="contact-icon"><svg width="12" height="12" viewBox="0 0 12 12"><path d="M2 1 L4.5 1 L5.5 3.8 L4 5 Q5 7.2 7 8 L8.2 6.5 L11 7.5 L11 10 Q5 11 1 3 Z" fill="#1c1c1e"/></svg></span>
        +0100 555 0147
      </li>
      <li class="contact-item">
        <span class="contact-icon"><svg width="14" height="14" viewBox="0 0 14 14" fill="none" stroke="#1c1c1e"><circle cx="7" cy="7" r="6"/><ellipse cx="7" cy="7" rx="2.6" ry="6"/><line x1="1" y1="7" x2="13" y2="7"/></svg></span>
        www.halvorfin.com
      </li>
    </ul>
  </article>

  <article class="card card-back">
    <svg class="card-shapes" viewBox="0 0 360 620" aria-hidden="true">
      <polygon points="360,170 360,620 130,620 130,300" fill="var(--accent-red)"/>
      <polygon points="60,300 330,175 130,300" fill="var(--accent-red)"/>
      <polygon points="80,296 345,205 340,214 100,300" fill="var(--card-black)"/>
    </svg>
    <div class="brand"><span class="brand-dot"></span>Halvor Finance</div>
    <div class="web-line">
      <span class="contact-icon"><svg width="14" height="14" viewBox="0 0 14 14" fill="none" stroke="#ffffff"><circle cx="7" cy="7" r="6"/><ellipse cx="7" cy="7" rx="2.6" ry="6"/><line x1="1" y1="7" x2="13" y2="7"/></svg></span>
      www.halvorfin.com
    </div>
  </article>

</main>
</body>
</html>
```